Letterhead for small civil engineer company

We need bold and modern design for company letterhead in MS word. It needs to have company logo and company info. Somewhere in the upper right part of document needs to be space for "recever" and the documents starts with, example, "SUBJECT: CIVIL ENGINEER LETTERHEAD".

in the bottom part of document needs to be signature and date.

Company info: Vrelon d.o.o., Dravunja 47, Lorvica (Općina Brelanj), OIB 47392615084, www.vrelon.hr, info@vrelon.hr

Email of document sender needs to be somewhere if document, exapmle xyz@vrelo.hr

Target Market(s)

Civil engineer company and projects

Industry/Entity Type

Civil engineer

Font styles to use
Serif

Colors
F0912C
F2A743
F7CA91
FBE8D2
FDF5EE

Requirements
Must have
• Company logo and company info
Nice to have
• Moder and clean design
Should not have
• Too much details

```html
<!DOCTYPE html>
<html lang="hr">
<head>
<meta charset="utf-8">
<title>Vrelon letterhead</title>
<link rel="stylesheet" href="https://fonts.googleapis.com/css2?family=Tinos:wght@400;700&family=PT+Sans&family=Great+Vibes&display=swap">
<style>
  :root {
    --orange: #F0912C;
    --orange-mid: #F2A743;
    --orange-soft: #F7CA91;
    --cream: #FBE8D2;
    --paper: #ffffff;
    --ink: #111111;
    --rule: #c8c8c8;
    --label-red: #e0304e;
    --sketch: #e8e8e8;
  }
  html, body { margin: 0; padding: 0; overflow: hidden; }
  body { width: 848px; height: 1200px; background: var(--paper); }
  .letterhead {
    position: relative; width: 848px; height: 1200px; overflow: hidden;
    background: var(--paper); font-family: "Tinos", serif; color: var(--ink);
  }
  .building-sketch {
    position: absolute; left: 300px; top: 613px; width: 548px; height: 563px;
    background: linear-gradient(180deg, rgba(232,232,232,0) 0%, rgba(232,232,232,0.55) 55%, rgba(228,228,228,0.8) 100%);
    -webkit-mask-image: linear-gradient(90deg, transparent 0%, #000 35%);
    mask-image: linear-gradient(90deg, transparent 0%, #000 35%);
  }
  .brand {
    position: absolute; left: 100px; top: 116px; display: flex; align-items: center; gap: 10px;
  }
  .brand-mark { width: 22px; height: 22px; background: var(--orange); }
  .brand-name {
    font-family: "Tinos", serif; font-size: 27px; letter-spacing: 2px; color: var(--orange); line-height: 1;
  }
  .rule { position: absolute; left: 100px; width: 648px; height: 3px; background: var(--rule); }
  .rule::before { content: ""; position: absolute; left: 0; top: 0; width: 61px; height: 3px; background: var(--orange); }
  .rule--top { top: 173px; }
  .rule--bottom { top: 1078px; }
  .company-info { position: absolute; left: 100px; top: 211px; font-size: 13px; line-height: 21.5px; }
  .company-info__label { color: var(--label-red); }
  .receiver, .date {
    position: absolute; left: 601px; font-family: "PT Sans", sans-serif; font-size: 12.5px;
  }
  .receiver { top: 211px; }
  .date { top: 936px; }
  .subject { position: absolute; left: 100px; top: 366px; font-size: 13px; font-weight: 700; margin: 0; }
  .signature { position: absolute; left: 98px; top: 885px; }
  .signature__name { font-family: "Great Vibes", cursive; font-size: 32px; line-height: 1; }
  .signature__label { font-size: 13px; margin-top: 2px; }
  .footer-contact { position: absolute; left: 319px; top: 1108px; display: flex; align-items: center; gap: 14px; }
  .footer-contact__text { font-size: 13px; line-height: 17px; }
  .footer-band { position: absolute; left: 0; bottom: 0; width: 848px; height: 24px; background: var(--orange); }
</style>
</head>
<body>
<div class="letterhead">
  <div class="building-sketch" role="img" aria-label="Faint line drawing of a modern building"></div>

  <div class="brand">
    <span class="brand-mark"></span>
    <span class="brand-name">VRELON</span>
  </div>
  <div class="rule rule--top"></div>

  <div class="company-info">
    <div class="company-info__label">Company info:</div>
    <div>Vrelon d.o.o., Dravunja 47,</div>
    <div>Lorvica (Općina Brelanj),</div>
    <div>OIB 47392615084</div>
  </div>
  <div class="receiver">Recever:-</div>

  <h1 class="subject">SUBJECT: CIVIL ENGINEER LETTERHEAD</h1>

  <div class="signature">
    <div class="signature__name">Marko Delin</div>
    <div class="signature__label">signature</div>
  </div>
  <div class="date">Date:-</div>

  <div class="rule rule--bottom"></div>
  <div class="footer-contact">
    <svg width="32" height="26" viewBox="0 0 32 26" aria-hidden="true">
      <rect x="1.5" y="1.5" width="29" height="23" rx="2" fill="none" stroke="var(--orange)" stroke-width="2"/>
      <path d="M2 3 L16 15 L30 3 M2 23 L12 13 M30 23 L20 13" fill="none" stroke="var(--orange)" stroke-width="2"/>
    </svg>
    <div class="footer-contact__text">
      <div>www.vrelon.hr,</div>
      <div>info@vrelon.hr</div>
    </div>
  </div>
  <div class="footer-band"></div>
</div>
</body>
</html>
```